Zentrix Banner Grid Ads for Custom Software Company

We need some images for display on the Zentrix Banner Grid. Need a collection of them at different sizes.

This is for a custom software development company that specializes in small to medium size businesses.

PLEASE PLEASE PLEASE GET CREATIVE! That is the point! Something very typical and plain will not win!

Target Market(s)

Small and Medium sized businesses looking for custom software development services

Industry/Entity Type

Computer Software

Font styles to use
Serif
Sans Serif

Requirements
Must have
• Medium Rectangle (300×250)
• Large Rectangle (336×280)
• Leaderboard (728×90)
• Half Page (300×600)
• Large Mobile Banner (320×100)
• Needs to stand out, but not be obnoxious
• Needs to flow with the website design and colors (does not need to be the same colors, just needs to work together)
• Must have specific call to action (schedule appointment or read more are options, but feel free to make up more)
Nice to have
• Logo integration
• Adobe Illustrator files with artboards/exports for the different sizes
Should not have
• Should not have more than 20% text
• Don't steal from the slides on the website. We want "read more" to mean read more, not more of the same.

```html
<!DOCTYPE html>
<html lang="en">
<head>
<meta charset="utf-8">
<title>Nexolva Software – Zentrix Banner Grid Set</title>
<link rel="stylesheet" href="https://fonts.googleapis.com/css2?family=Montserrat:wght@500;600;700&display=swap">
<style>
:root{
  --stage:#2b2b2b;
  --panel:#e7e7e9;
  --blue-deep:#0b4fa3;
  --blue:#1a6fba;
  --blue-bright:#2aa9e0;
  --cta:#3cbde9;
  --cta-text:#0b1e33;
  --photo-light:#d9d6d2;
  --photo-mid:#8f97a3;
  --photo-dark:#2f3a4d;
}
*{margin:0;padding:0;box-sizing:border-box}
html,body{width:1200px;height:900px;overflow:hidden;background:var(--stage)}
body{position:relative;font-family:"Montserrat",Arial,sans-serif}
.banner{position:absolute;overflow:hidden;background:var(--panel)}
.banner > svg.art{position:absolute;inset:0;width:100%;height:100%}
.brand{position:absolute;display:flex;align-items:center;gap:6px;color:var(--blue);font-weight:500;white-space:nowrap}
.brand-mark{background:var(--blue-bright);display:block}
.headline{position:absolute;color:var(--blue);font-weight:700;text-transform:uppercase;text-align:center;line-height:1.2;letter-spacing:.5px}
.cta{position:absolute;background:var(--cta);color:var(--cta-text);font-weight:600;border-radius:8px;display:flex;align-items:center;justify-content:center;white-space:nowrap;box-shadow:0 2px 0 rgba(11,79,163,.35)}
.contact{position:absolute;color:var(--blue);font-weight:600;text-align:center;white-space:nowrap}

.medium{left:74px;top:233px;width:300px;height:250px}
.large{left:424px;top:218px;width:336px;height:280px}
.halfpage{left:835px;top:137px;width:300px;height:600px}
.leaderboard{left:63px;top:556px;width:720px;height:90px}
.mobile{left:241px;top:703px;width:320px;height:100px}
</style>
</head>
<body>

<svg width="0" height="0" style="position:absolute">
  <defs>
    <linearGradient id="photoTone" x1="0" y1="0" x2="1" y2="0.4">
      <stop offset="0" stop-color="#e4e1dc"/>
      <stop offset=".45" stop-color="#9aa1ab"/>
      <stop offset="1" stop-color="#3a4558"/>
    </linearGradient>
    <linearGradient id="bandDeep" x1="0" y1="0" x2="1" y2="0">
      <stop offset="0" stop-color="#0b4fa3"/>
      <stop offset="1" stop-color="#1a6fba"/>
    </linearGradient>
    <linearGradient id="bandBright" x1="0" y1="0" x2="1" y2="0">
      <stop offset="0" stop-color="#1a7fcc"/>
      <stop offset="1" stop-color="#35c3ec"/>
    </linearGradient>
  </defs>
</svg>

<!-- Medium Rectangle 300x250 -->
<section class="banner medium">
  <svg class="art" viewBox="0 0 300 250" preserveAspectRatio="none">
    <rect width="300" height="160" fill="url(#photoTone)" role="img" aria-label="Photo of two business colleagues reviewing work at a desk"/>
    <polygon points="0,108 150,86 300,110 300,124 150,100 0,122" fill="url(#bandDeep)"/>
    <polygon points="0,134 150,110 300,136 300,150 150,124 0,148" fill="url(#bandBright)"/>
    <polygon points="0,156 150,132 300,158 300,250 0,250" fill="var(--panel)"/>
    <polygon points="0,190 60,250 42,250 0,208" fill="url(#bandDeep)"/>
    <polygon points="0,218 32,250 14,250 0,236" fill="url(#bandBright)"/>
    <polygon points="300,186 236,250 254,250 300,204" fill="url(#bandDeep)"/>
    <polygon points="300,214 268,250 286,250 300,232" fill="url(#bandBright)"/>
  </svg>
  <div class="brand" style="left:9px;top:24px;font-size:22px"><span class="brand-mark" style="width:30px;height:30px"></span>Nexolva</div>
  <div class="headline" style="left:0;width:300px;top:160px;font-size:16px">The # 1 Solution for<br>Outstanding Results</div>
  <div class="cta" style="left:92px;top:205px;width:122px;height:20px;font-size:7.5px">Schedule Appointment Today</div>
  <div class="contact" style="left:0;width:300px;top:232px;font-size:7.5px">(555) 014-2290 | https://nexolva.example</div>
</section>

<!-- Large Rectangle 336x280 -->
<section class="banner large">
  <svg class="art" viewBox="0 0 336 280" preserveAspectRatio="none">
    <rect width="336" height="180" fill="url(#photoTone)" role="img" aria-label="Photo of two business colleagues reviewing work at a desk"/>
    <polygon points="0,138 168,102 336,128 336,142 168,116 0,152" fill="url(#bandDeep)"/>
    <polygon points="0,164 168,128 336,154 336,168 168,142 0,178" fill="url(#bandBright)"/>
    <polygon points="0,184 168,150 336,176 336,280 0,280" fill="var(--panel)"/>
    <polygon points="0,218 62,280 44,280 0,236" fill="url(#bandDeep)"/>
    <polygon points="0,246 34,280 16,280 0,264" fill="url(#bandBright)"/>
    <polygon points="336,214 270,280 288,280 336,232" fill="url(#bandDeep)"/>
    <polygon points="336,242 298,280 316,280 336,260" fill="url(#bandBright)"/>
  </svg>
  <div class="brand" style="left:9px;top:28px;font-size:24px"><span class="brand-mark" style="width:34px;height:34px"></span>Nexolva</div>
  <div class="headline" style="left:0;width:336px;top:182px;font-size:16px">The # 1 Solution for<br>Outstanding Results</div>
  <div class="cta" style="left:104px;top:230px;width:136px;height:24px;font-size:8px">Schedule Appointment Today</div>
  <div class="contact" style="left:0;width:336px;top:261px;font-size:8.5px">(555) 014-2290 | https://nexolva.example</div>
</section>

<!-- Half Page 300x600 -->
<section class="banner halfpage">
  <svg class="art" viewBox="0 0 300 600" preserveAspectRatio="none">
    <rect width="300" height="340" fill="url(#photoTone)" role="img" aria-label="Photo of two business colleagues reviewing a document together"/>
    <polygon points="0,262 150,182 300,262 300,282 150,204 0,282" fill="url(#bandDeep)"/>
    <polygon points="0,296 150,222 300,296 300,318 150,244 0,318" fill="url(#bandBright)"/>
    <path d="M0,335 Q150,240 300,335 L300,600 L0,600 Z" fill="var(--panel)"/>
    <rect y="565" width="300" height="12" fill="url(#bandDeep)"/>
    <rect y="581" width="300" height="19" fill="url(#bandBright)"/>
  </svg>
  <div class="brand" style="left:52px;top:316px;font-size:32px"><span class="brand-mark" style="width:44px;height:44px"></span>Nexolva</div>
  <div class="headline" style="left:0;width:300px;top:396px;font-size:21px;line-height:1.2">The # 1 Solution<br>for<br><span style="font-size:17px">Outstanding Results</span></div>
  <div class="cta" style="left:45px;top:479px;width:211px;height:37px;font-size:12px">Schedule Appointment Today</div>
  <div class="contact" style="left:0;width:300px;top:533px;font-size:12.5px">(555) 014-2290 | https://nexolva.example</div>
</section>

<!-- Leaderboard 728x90 (shown 720x90) -->
<section class="banner leaderboard">
  <svg class="art" viewBox="0 0 720 90" preserveAspectRatio="none">
    <rect width="320" height="90" fill="url(#photoTone)" role="img" aria-label="Photo of a businessman reviewing work at a desk"/>
    <polygon points="235,0 256,0 212,45 256,90 235,90 191,45" fill="url(#bandDeep)"/>
    <polygon points="262,0 280,0 236,45 280,90 262,90 218,45" fill="url(#bandBright)"/>
    <path d="M300,0 L720,0 L720,90 L300,90 Q240,45 300,0 Z" fill="var(--panel)"/>
    <polygon points="284,0 300,0 262,45 300,90 284,90 246,45" fill="url(#bandDeep)"/>
    <rect x="700" width="6" height="90" fill="url(#bandDeep)"/>
    <rect x="710" width="10" height="90" fill="url(#bandBright)"/>
  </svg>
  <div class="brand" style="left:10px;top:28px;font-size:22px"><span class="brand-mark" style="width:30px;height:30px"></span>Nexolva</div>
  <div class="headline" style="left:286px;width:262px;top:15px;font-size:16.5px">The # 1 Solution for<br>Outstanding Results</div>
  <div class="cta" style="left:555px;top:33px;width:135px;height:24px;font-size:8px">Schedule Appointment Today</div>
  <div class="contact" style="left:286px;width:262px;top:63px;font-size:10.5px">(555) 014-2290 | https://nexolva.example</div>
</section>

<!-- Large Mobile Banner 320x100 -->
<section class="banner mobile">
  <svg class="art" viewBox="0 0 320 100" preserveAspectRatio="none">
    <rect width="150" height="100" fill="url(#photoTone)" role="img" aria-label="Photo of a desk meeting with coffee cups"/>
    <polygon points="104,0 122,0 82,50 122,100 104,100 64,50" fill="url(#bandDeep)"/>
    <polygon points="126,0 140,0 100,50 140,100 126,100 86,50" fill="url(#bandBright)"/>
    <path d="M150,0 L320,0 L320,100 L150,100 Q100,50 150,0 Z" fill="var(--panel)"/>
    <rect x="303" width="4" height="100" fill="url(#bandDeep)"/>
    <rect x="310" width="10" height="100" fill="url(#bandBright)"/>
  </svg>
  <div class="brand" style="left:6px;top:16px;font-size:13px;gap:4px"><span class="brand-mark" style="width:17px;height:17px"></span>Nexolva</div>
  <div class="headline" style="left:140px;width:160px;top:20px;font-size:10px">The # 1 Solution for<br>Outstanding Results</div>
  <div class="cta" style="left:173px;top:53px;width:94px;height:17px;font-size:5.5px;border-radius:6px">Schedule Appointment Today</div>
  <div class="contact" style="left:140px;width:160px;top:79px;font-size:6.5px">(555) 014-2290 | https://nexolva.example</div>
</section>

</body>
</html>
```